Redesign of an insurance website

Attached is an insurance website that I need to redesign. Currently the website is too dark. I like for example www.brenvalo.com . Could you make the website lighter and change the structure a little so that it is more user friendly?

Industry/Entity Type

Insurance

Number of Pages Required

4 page

```html
<!DOCTYPE html>
<html lang="en">
<head>
<meta charset="utf-8">
<title>Krytovka.cz – Insurance</title>
<link href="https://fonts.googleapis.com/css2?family=Lato:wght@300;400;700&family=Roboto:wght@300;400;500;700&display=swap" rel="stylesheet">
<style>
:root{
  --orange:#fd7a15;
  --blue:#2a7ff0;
  --ink:#222;
  --muted:#666;
  --light-bg:#f6f7f9;
  --band-bg:#e9eaec;
  --footer-bg:#1e1e1e;
  --white:#fff;
}
*{box-sizing:border-box;margin:0;padding:0}
html,body{width:1200px;height:1066px;overflow:hidden}
body{position:relative;font-family:'Roboto',sans-serif;color:var(--ink);background:var(--white)}
.abs{position:absolute}
.brand{font-family:'Roboto',sans-serif;font-weight:700;font-size:24px;letter-spacing:1px;color:var(--blue)}
.site-header{position:absolute;left:0;top:0;width:1200px;height:67px;background:var(--white)}
.site-header .brand{left:150px;top:19px}
.main-nav{left:622px;top:28px;font-size:12px;color:#333;display:flex;gap:14px}
.main-nav .active{color:var(--blue)}
.main-nav .sep{color:#777}
.btn{position:absolute;display:flex;align-items:center;justify-content:center;color:var(--white);font-size:12px}
.btn-orange{background:var(--orange)}
.btn-blue{background:var(--blue)}
.hero{position:absolute;left:0;top:67px;width:1200px;height:420px;
  background:linear-gradient(180deg,#e9e1d6 0%,#d9c6ae 30%,#b79d84 62%,#6b5d55 100%)}
.hero-photo{position:absolute;inset:0;
  background:radial-gradient(ellipse 260px 200px at 430px 80px,rgba(255,240,210,.9),rgba(255,240,210,0) 70%),
  linear-gradient(90deg,rgba(80,60,50,.25),rgba(0,0,0,0) 40%,rgba(0,0,0,0) 70%,rgba(255,255,255,.1))}
.social{left:0;top:134px;width:26px}
.social span{display:block;width:26px;height:26px}
.hero-title{left:157px;top:316px;font-size:18px;font-weight:500;color:var(--white)}
.hero-list{list-style:none;color:var(--white);font-size:11.5px;font-weight:300;line-height:18px}
.hero-list li::before{content:"";display:inline-block;width:0;height:0;border-left:5px solid var(--orange);border-top:4px solid transparent;border-bottom:4px solid transparent;margin-right:7px}
.quote-card{left:810px;top:56px;width:232px;height:307px;background:rgba(244,242,240,.93);padding:12px 11px}
.quote-card h2{font-family:'Lato',sans-serif;font-weight:700;font-size:24px;color:#2a2a2a;margin:0 0 13px 4px}
.field{height:23px;border:1px solid #bcbcbc;background:#fff;font-size:9px;color:#777;padding:6px 5px;margin:0 0 7px 4px}
.consent{font-size:8.5px;color:#555;margin:8px 0 0 4px;display:flex;align-items:center;gap:5px}
.consent u{color:#444}
.submit{margin:12px 0 0 4px;height:26px;background:var(--orange);color:#fff;font-weight:700;font-size:11px;display:flex;align-items:center;justify-content:center}
.products{display:flex;margin:10px 0 0 4px;justify-content:space-between}
.product{width:56px;text-align:center;font-size:9px;color:#666;line-height:13px}
.product svg{display:block;margin:0 auto 2px}
.pager{position:absolute;right:16px;bottom:21px;display:flex;gap:4px}
.pager span{width:20px;height:20px;border:1px solid #666;display:flex;align-items:center;justify-content:center}
.pager .next{background:#555}
.features{position:absolute;left:0;top:487px;width:1200px;height:339px;background:var(--light-bg)}
.feature-title{font-family:'Lato',sans-serif;font-weight:300;font-size:25px;color:#333}
.lead{font-size:11px;font-weight:500;color:#222;line-height:17px}
.body-text{font-size:11px;font-weight:300;color:#555;line-height:16px}
.feature-image{left:534px;top:66px;width:261px;height:189px;background:radial-gradient(circle at 118px 82px,#a08640 0,#3a3a30 12%,#1c2230 45%,#0e121a 100%)}
.newsletter{position:absolute;left:0;top:826px;width:1200px;height:144px;background:var(--band-bg)}
.newsletter h3{position:absolute;left:157px;top:56px;font-family:'Lato',sans-serif;font-weight:300;font-size:26px;color:#333}
.email-input{left:458px;top:58px;width:440px;height:30px;background:#fff;font-size:11px;color:#777;padding:9px 16px}
.site-footer{position:absolute;left:0;top:970px;width:1200px;height:96px;background:var(--footer-bg)}
.site-footer .brand{left:150px;top:34px}
.legal{right:150px;top:42px;font-size:11px;font-weight:300;color:#999}
.legal a{color:var(--blue);text-decoration:none}
</style>
</head>
<body>
<header class="site-header">
  <div class="abs brand">KRYTOVKA.CZ</div>
  <nav class="abs main-nav"><span class="active">Home</span><span class="sep">/</span><span>About Us</span><span class="sep">/</span><span>Contact Us</span></nav>
  <a class="btn btn-orange" style="left:862px;top:20px;width:90px;height:27px">Lorem ipsum</a>
  <a class="btn btn-blue" style="left:960px;top:20px;width:90px;height:27px">Aliquam elit</a>
</header>

<section class="hero">
  <div class="hero-photo" role="img" aria-label="Photo of a woman with outstretched arms facing a sunlit city skyline"></div>
  <div class="abs social"><span style="background:#3b5a98"></span><span style="background:#d34836"></span><span style="background:#2aa3ef"></span></div>
  <h1 class="abs hero-title">Lorem ipsum dolor sit amet</h1>
  <ul class="abs hero-list" style="left:157px;top:345px">
    <li>Aliquam elit nibh, mattis in enim</li>
    <li>Etiam eleifend ligula in quam luctus</li>
    <li>Cras est diam, mattis sit amet hendrerit</li>
  </ul>
  <ul class="abs hero-list" style="left:381px;top:345px">
    <li>Integer nec risus id sapien scelerisque viverra</li>
    <li>Morbi iaculis ligula eu velit accumsan ullamcorper</li>
    <li>Quisque a nibh convallis, porta ipsum ornare</li>
  </ul>
  <form class="abs quote-card">
    <h2>Integer nec risus</h2>
    <div class="field">Name:</div>
    <div class="field">Phone:</div>
    <div class="field">Email:</div>
    <div class="consent"><svg width="9" height="9" viewBox="0 0 9 9"><rect x=".5" y=".5" width="8" height="8" fill="#fff" stroke="#666"/><path d="M2 4.5l2 2 3-4.5" stroke="#222" fill="none" stroke-width="1.3"/></svg>Curabitur <u>laoreet sem accumsan</u></div>
    <div class="submit">SUBMIT</div>
    <div class="products">
      <div class="product"><svg width="22" height="14" viewBox="0 0 22 14"><path d="M3 7l3-5h10l3 5v5H3z" fill="none" stroke="#f0a030" stroke-width="1.5"/><circle cx="7" cy="12" r="1.5" fill="#f0a030"/><circle cx="15" cy="12" r="1.5" fill="#f0a030"/></svg>Aliquam Elit</div>
      <div class="product"><svg width="24" height="14" viewBox="0 0 24 14"><path d="M2 8h18l3-2-3 4H4z M10 8l4-5h2l-2 5z" fill="#3cb4e8"/></svg>Integer nec</div>
      <div class="product"><svg width="20" height="16" viewBox="0 0 20 16"><path d="M2 8l8-7 8 7z" fill="#d43a2a"/><rect x="4" y="8" width="12" height="8" fill="#eee" stroke="#999"/><rect x="8" y="11" width="4" height="5" fill="#3a8a3a"/></svg>Curabitur laoreet</div>
      <div class="product"><svg width="24" height="14" viewBox="0 0 24 14"><rect x="1" y="2" width="22" height="9" rx="2" fill="#b02a2a"/><rect x="4" y="4" width="14" height="3" fill="#eee"/><circle cx="6" cy="12" r="2" fill="#333"/><circle cx="18" cy="12" r="2" fill="#333"/></svg>Aliquam Elit</div>
    </div>
    <div class="pager">
      <span><svg width="8" height="10"><path d="M6 1L2 5l4 4" stroke="#444" fill="none"/></svg></span>
      <span class="next"><svg width="8" height="10"><path d="M2 1l4 4-4 4" stroke="#fff" fill="none"/></svg></span>
    </div>
  </form>
</section>

<section class="features">
  <h2 class="abs feature-title" style="left:158px;top:60px">Lorem ipsum dolor sit amet</h2>
  <p class="abs lead" style="left:159px;top:93px">Aliquam elit nibh, mattis in enim eu, semper congue ipsum.</p>
  <p class="abs body-text" style="left:159px;top:117px;width:355px">Lorem ipsum dolor sit amet, consectetur scing elit. Pellentesque at felis magna. Etiam auctor risus non enim vehicula, a tincidunt diam aliquet. Maecenas nisl urna, elementum at dolor quis, convallis iaculis massa. Sed laoreet lacus ut sodales auctor. Donec libero orci, malesuada sed risus vitae, volutpat elementum tortor.</p>
  <a class="btn btn-orange" style="left:158px;top:226px;width:95px;height:29px;font-weight:700;font-size:11px">READ MORE</a>
  <div class="abs feature-image" role="img" aria-label="Close-up photo of golden clock hands on a dark dial"></div>
  <h2 class="abs feature-title" style="left:834px;top:60px">Sed commodo sagittis</h2>
  <p class="abs lead" style="left:834px;top:93px;width:210px">Aliquam elit nibh, mattis in enim eu, semper congue ipsum.</p>
  <p class="abs body-text" style="left:834px;top:134px;width:210px">Lorem ipsum dolor sit amet, consectetur scing elit. Pellentesque at felis magna. Etiam auctor risus non enim vehicula, a tincidunt diam aliquet. Maecenas nisl urna, elementum at dolor quis, convallis iaculis massa. Sed laoreet lacus ut sodales auctor.</p>
</section>

<section class="newsletter">
  <h3>Integer nec risus id sapien</h3>
  <div class="abs email-input">Email:</div>
  <a class="btn btn-orange" style="left:908px;top:58px;width:134px;height:30px;font-weight:700;font-size:11px">SUBSCRIBE</a>
</section>

<footer class="site-footer">
  <div class="abs brand">KRYTOVKA.CZ</div>
  <p class="abs legal">Phasellus eu &nbsp;|&nbsp; Curabitur laoreet sem &nbsp;|&nbsp; © 2017 <a>Krytovka.cz</a>. All Right Reserved.</p>
</footer>
</body>
</html>
```